Stationary and Business Card for Talbe Media Company
Include Invoice, DVD and Binder template
Stationary and Business Card for Talbe Media Company -
Creative Brief
Use specific fonts
Prefer font name "neometric" ... you suggest
Professional
K. Morwenel
Sales Director
P. O. Box No 47318, Lam Fung Wan, Kowloon, Hong Kong
morwenel@talbe.example
www.talbe.example
at the back of the business card add the following tag "Smart Media Delivery Partner" make sure it is at one side in a small font . It can also, be added to the Stationaries.
In the Company's logo the letter "O" reflects our business .. we can have the "O" occupies most of the back and add to it the tag "Smart Media Delivery Partner" in a small font. you suggest

```html
<!DOCTYPE html>
<html lang="en">
<head>
<meta charset="utf-8">
<title>Talbe Media Company – Business Card</title>
<link rel="stylesheet" href="https://fonts.googleapis.com/css2?family=Montserrat:wght@400;500;600;700&family=Open+Sans:wght@400;600&display=swap">
<style>
  :root {
    --bg: #e4e1dc;
    --card-light: #ffffff;
    --card-light-edge: #f1f1f1;
    --card-dark-top: #4a4a4a;
    --card-dark-bottom: #262626;
    --brand-red: #c8141e;
    --text-grey: #6a6a6a;
    --text-dark: #444444;
    --faint: #ececec;
    --white: #ffffff;
  }
  html, body {
    margin: 0;
    padding: 0;
    width: 1200px;
    height: 971px;
    overflow: hidden;
    background: var(--bg);
    font-family: "Open Sans", Arial, sans-serif;
  }
  .canvas {
    position: relative;
    width: 1200px;
    height: 971px;
  }
  .card {
    position: absolute;
    width: 490px;
    height: 282px;
    box-shadow: 0 6px 18px rgba(0,0,0,0.28);
    overflow: hidden;
  }
  /* Front */
  .card-front {
    left: 387px;
    top: 184px;
    background: linear-gradient(180deg, var(--card-light) 0%, var(--card-light-edge) 100%);
  }
  .brand {
    position: absolute;
    left: 28px;
    top: 22px;
  }
  .brand-name {
    font-family: "Montserrat", Arial, sans-serif;
    font-weight: 500;
    font-size: 52px;
    line-height: 52px;
    letter-spacing: 1px;
    color: var(--brand-red);
  }
  .brand-tag {
    margin-top: 10px;
    font-size: 10px;
    color: var(--text-grey);
  }
  .front-mark {
    position: absolute;
    left: 270px;
    top: 40px;
  }
  .contact-name {
    position: absolute;
    left: 28px;
    top: 150px;
    font-family: "Montserrat", Arial, sans-serif;
    font-weight: 600;
    font-size: 19px;
    color: var(--brand-red);
  }
  .contact-title {
    position: absolute;
    left: 28px;
    top: 176px;
    font-size: 11px;
    color: var(--text-grey);
  }
  .contact-details {
    position: absolute;
    left: 28px;
    top: 218px;
    font-size: 11px;
    line-height: 19px;
    color: var(--text-dark);
  }
  .contact-details .label { color: var(--brand-red); }
  .contact-details .sep { color: var(--text-grey); padding: 0 4px; }
  /* Back */
  .card-back {
    left: 316px;
    top: 482px;
    background: radial-gradient(ellipse at 50% 35%, var(--card-dark-top) 0%, var(--card-dark-bottom) 80%);
  }
  .back-mark {
    position: absolute;
    left: 199px;
    top: 70px;
  }
  .back-company {
    position: absolute;
    left: 0;
    width: 100%;
    top: 172px;
    text-align: center;
    font-family: "Montserrat", Arial, sans-serif;
    font-weight: 500;
    font-size: 15px;
    line-height: 18px;
    letter-spacing: 2px;
    color: var(--brand-red);
  }
  .back-tag {
    position: absolute;
    left: 0;
    width: 100%;
    top: 200px;
    text-align: center;
    font-size: 13px;
    line-height: 18px;
    color: var(--white);
  }
</style>
</head>
<body>
<main class="canvas">
  <section class="card card-front">
    <div class="brand">
      <div class="brand-name">talbe</div>
      <div class="brand-tag">Smart Media Delivery Partner</div>
    </div>
    <svg class="front-mark" width="184" height="184" viewBox="0 0 184 184" aria-hidden="true">
      <circle cx="92" cy="92" r="90" fill="var(--faint)" opacity="0.7"/>
    </svg>
    <div class="contact-name">K. Morwenel</div>
    <div class="contact-title">Sales Director</div>
    <div class="contact-details">
      <div>P. O. Box No 47318, Lam Fung Wan, Kowloon, Hong Kong</div>
      <div><span class="label">Phone :</span> (852) 31004827 <span class="sep">|</span> <span class="label">Fax :</span> (852) 31004828</div>
      <div><span class="label">Email :</span> morwenel@talbe.example <span class="sep">|</span> <span class="label">Web :</span> www.talbe.example</div>
    </div>
  </section>

  <section class="card card-back">
    <svg class="back-mark" width="92" height="92" viewBox="0 0 92 92" aria-hidden="true">
      <circle cx="46" cy="46" r="44" fill="var(--white)"/>
    </svg>
    <div class="back-company">TALBE MEDIA COMPANY</div>
    <div class="back-tag">Smart Media Delivery Partner</div>
  </section>
</main>
</body>
</html>
```